Best-selling business author needs Next Craft Line book cover designs

We're launching a series of books and online training videos badged under the "Brightfork Notes - Next Craft Line" brand. The idea is that there are titles for each of the future skills that people will need to survive the robots in the future, eg, Creativity, Critical Thinking Skills, Problem Solving, etc. The exciting job here is to create a series thematic look, and a specific design for the first title, Sharp Prompts.
Hope my brief challenges you, and look forward to your questions and designs.

Target Market(s)

start ups and corporate market (mainly in Asia Pacific) looking to upskill themselves. Probably 18-45 age group, including uni business students, and people working in Meridian 400s.

Industry/Entity Type

Publishing Company

Font styles to use
Serif
Sans Serif
Other font styles liked:
• Felt marker or other 'handcrafted' styles because these will be 'workbook' style publications

Colors
ec1f27
3276b5
00a990
9bcb3c
fbed22
f78f20
6b449b

Requirements
Must have
• Must look professional but not boring or old school.
• Use the "Brightfork Notes Next Craft Line" (logo attached).
• Need category, ie "critical thinking" associated with logo above
• Need title and subtitle of the book, ie "SHARP PROMPTS. How to shape better questions to create explosive breakthroughs."
• All the type you see on sample design, ie reviewers blurb at top, author's name etc.
• Vivid and strong colour schemes to be eye -catching individually but especially strong when lined up on bookshelves together.
• See examples attached for QTV series (competitor) and also a quick design hack by myself to give an idea of what it "might" look like.
• A5 portrait format.
• Spine and Back page will be largely text (with barcode, see example).
• Back page text:
• Heading: Ways to Win the Modern Market with Bold Inquiry Habits.
• - Find out the Sharp Prompts that kick-started empires like NestLoop, Colby Hensel, Beanrowe, Vitalume, Sky Orin, Melodex, Zentrix, Orbely, Tobin Wexley, and even Fundquill.
• - Learn how companies like R&T, Quince, Varlo, AeroMint, Fablon, Lyra, Caravel R3, Movra, and Tulp use Sharp Prompts to develop blockbuster new products, experiences and marketing messages.
• - How to identify and eradicate your cognitive blindspots.
• - How to create a Curiosity Gap (and why that’s so important).
• - Why it’s important to challenge the Status Quo, and how to do it.
• Heading: What if there was a formula for creating Sharp Prompts? There is!
• Get on board this rocket ship with business creativity expert (and best-selling author) Reg Mannix as he guides you through a proven system for creating more insightful, more powerful questions, which point us toward breakthrough solutions, products, and process innovations.
• For the first time, he shares the Sharp Prompts (Discovery Prompt Building Method) here. The same system that he has taught to senior executives from major corporations such as Norvale Bank, Strivon, KessmarFahr, Medwyn, Tolvax, and many other progressive companies.
• Heading: Praise for Sharp Prompts
• “Really enjoyed Sharp Prompts. Like taking a peek into the minds of some of the greatest innovators right as they were asking these SHARP PROMPTS that prompted them to create history!” Rohan Dutt, Head of R&D, Quartel China.
• “Awesome! It’s a great book, I’m a huge fan of the power of questions.” Gavin Hoskins, VP, Norvale Bank.
• "Sharp Prompts is a Sharp Book! This has really helped with both my classroom sessions and consulting projects. Well done!"
• Martin Esterhal, Adj. Professor, The University of Bramcote.
• www.regmannix.example #sharp prompts
• [insert bar code]
Nice to have
• Prefer simple strong bold graphic approach.
• Using photos, or icons to highlight the topic. Please avoid cliches.
Should not have
• Not overly fancy, ornate, or visually complicated.

```html
<!DOCTYPE html>
<html lang="en">
<head>
<meta charset="utf-8">
<title>Sharp Prompts – Book Cover</title>
<link rel="stylesheet" href="https://fonts.googleapis.com/css2?family=Open+Sans:wght@600;700;800&family=Roboto+Slab:wght@400;800&display=swap">
<style>
  :root {
    --stage: #e4e5e1;
    --paper: #f3f3f1;
    --signal-red: #e4282b;
    --quote-red: #d81f26;
    --ink: #151515;
    --white: #ffffff;
    --grey: #8d8d8d;
    --flame: #f78f20;
    --gold: #fbd90f;
  }
  * { box-sizing: border-box; margin: 0; padding: 0; }
  html, body { width: 1200px; height: 1200px; overflow: hidden; }
  body { background: var(--stage); position: relative; font-family: "Open Sans", Arial, sans-serif; }

  .cover {
    position: absolute; left: 215px; top: 50px;
    width: 770px; height: 1100px;
    background: var(--paper); overflow: hidden;
  }
  .cover__lower {
    position: absolute; left: 0; top: 395px; width: 100%; height: 705px;
    background: var(--signal-red);
  }

  .blurb {
    position: absolute; left: 20px; right: 20px; top: 22px;
    font-family: "Roboto Slab", Georgia, serif; font-weight: 800;
    font-size: 20px; line-height: 28px; color: var(--quote-red);
    text-align: center; letter-spacing: 0.2px;
  }

  .series-mark {
    position: absolute; left: 8px; top: 190px;
    display: flex; align-items: center; gap: 8px;
  }
  .series-mark__dot { width: 44px; height: 44px; border-radius: 50%; background: var(--flame); }
  .series-mark__name {
    font-family: "Open Sans", Arial, sans-serif; font-weight: 700;
    font-size: 37px; line-height: 1; color: var(--ink); letter-spacing: -0.5px;
  }
  .series-line {
    position: absolute; left: 74px; top: 236px;
    font-family: "Roboto Slab", Georgia, serif; font-weight: 400;
    font-size: 17px; color: var(--ink); letter-spacing: 0.3px;
    border-top: 2px solid var(--grey); padding-top: 2px; width: 280px;
  }
  .category {
    position: absolute; left: 4px; top: 276px;
    font-family: "Open Sans", Arial, sans-serif; font-weight: 700;
    font-size: 34px; letter-spacing: 0.5px;
  }
  .category__muted { color: var(--grey); }
  .category__strong { color: var(--ink); }

  .question-art {
    position: absolute; left: 530px; top: 150px; width: 240px; height: 235px;
  }
  .bomb-art {
    position: absolute; left: 612px; top: 398px; width: 84px; height: 84px;
  }

  .title {
    position: absolute; left: 0; width: 100%; text-align: center;
    font-family: "Open Sans", Arial, sans-serif; font-weight: 800; line-height: 1;
  }
  .title--top { top: 474px; font-size: 132px; color: var(--ink); letter-spacing: -2px; padding-right: 40px; }
  .title--bottom { top: 598px; font-size: 108px; color: var(--white); letter-spacing: -1px; }

  .subtitle {
    position: absolute; left: 0; top: 722px; width: 100%; text-align: center;
    font-family: "Open Sans", Arial, sans-serif; font-weight: 700;
    font-size: 52px; line-height: 62px; letter-spacing: -0.8px; white-space: nowrap;
  }
  .subtitle .dark { color: var(--ink); }
  .subtitle .light { color: var(--white); }

  .divider {
    position: absolute; left: 184px; top: 918px; width: 374px; height: 2px; background: var(--paper);
  }
  .author {
    position: absolute; left: 0; top: 936px; width: 100%; text-align: center;
    font-family: "Open Sans", Arial, sans-serif; font-weight: 700;
    font-size: 43px; color: var(--ink);
  }
  .author-tags {
    position: absolute; left: 0; top: 1000px; width: 100%; text-align: center;
    font-family: "Open Sans", Arial, sans-serif; font-weight: 700;
    font-size: 27px; color: var(--gold);
  }
</style>
</head>
<body>
  <main class="cover">
    <div class="cover__lower"></div>

    <p class="blurb">“MORE STIMULATING THAN A DOUBLE SHOT OF COLD<br>BREW INFUSED COFFEE FULL OF ENERGY, FRESH AND<br>BRIGHT IDEAS”.<br>OWEN CALDER, FELLOW, KVR.</p>

    <div class="series-mark">
      <span class="series-mark__dot"></span>
      <span class="series-mark__name">Brightfork Notes</span>
    </div>
    <p class="series-line">NEXT CRAFT LINE &gt;&gt;&gt;</p>
    <p class="category"><span class="category__muted">CRITICAL</span> <span class="category__strong">THINKING</span></p>

    <svg class="question-art" viewBox="0 0 240 235" role="img" aria-label="Illustration of a large grey question mark">
      <defs>
        <linearGradient id="artTone" x1="0" y1="0" x2="0" y2="1">
          <stop offset="0" stop-color="#7a7a7a"/>
          <stop offset="1" stop-color="#5a5a5a"/>
        </linearGradient>
      </defs>
      <rect x="0" y="0" width="240" height="235" rx="16" fill="url(#artTone)"/>
    </svg>
    <svg class="bomb-art" viewBox="0 0 84 84" role="img" aria-label="Illustration of a round black bomb with a lit fuse, forming the dot of the question mark">
      <circle cx="42" cy="42" r="40" fill="#3a3a3a"/>
    </svg>

    <h1 class="title title--top">SHARP</h1>
    <h1 class="title title--bottom">PROMPTS</h1>

    <p class="subtitle">
      <span class="dark">How to</span> <span class="light">shape better</span><br>
      <span class="light">questions</span> <span class="dark">to create explosive</span><br>
      <span class="light">breakthroughs</span>
    </p>

    <div class="divider"></div>
    <p class="author">Reg Mannix</p>
    <p class="author-tags">Summit MC &nbsp;| Storyteller | Sparkmaker</p>
  </main>
</body>
</html>
```